Investment online portal styling and design elements

We would like to design an online portal that our clients will use to access their personal investment information. Our business is Brenwick Capital Advisors (http://www.brenwickcapitaladvisors.example/).

We are part of a large law firm and have been in business for 100 + years. Our clients are successful families who are seeking to manage their wealth in a diversified and global investment portfolio. We are preparing new investment reports and an accompanying online portal to present the investment information. This project is for the design and styling of the Summary page and Portfolio page (the style sheet and design elements for which can be transferred across the portal to all other pages) of a web portal that we have purchased from a vendor. The portal design should contain three content ideas: (1) that this is a Brenwick Capital Advisors Account Portal, (2) the name of the account and (3) the account number .

Proposals should assume HTML5 and CSS3 styling. We have determined that this portal should use menu-driven navigation. The menu should be presented consistently through the site and include:

1) Summary (which would include basic high level account details, like first page of the attached pdf)

2) Portfolio (which would include specifics into what the client’s assets are, in particular pages 2 and 3 of the attached pdf)

3) Performance

4) Holdings and Activity

5) Documents and Mail

6) My Profile

The content on each portal page will be controlled by the web portal technology we have purchased for this purpose.

RGB for the firm's colors are:
#33a6d7
#aaaaaa
#5c5c5c
#000000

Please refer to our website to see the design concepts used by the firm. I have attached the newly-designed set of client reports which we will introduce simultaneously with the portal. The charts, graphs, tables, etc. in these reports will be presented identically in the online portal. You should take into account our firm logo and the blue color, but you do not need to mimic the report design or the firm’s website design, although they should be able to coexist cohesively. We would like the portal to follow our overall, simple design ethic but reflect the fact that this is a fresh, new interface. I have also uploaded a pdf file of the final version of the first few pages of the reports. You can use the content in these pages for your design, if helpful. Thank you.

Target Market(s)

Clients who are investors

Industry/Entity Type

Financial Service

Coding

Number of Pages Required

1 page

Font styles to use
Sans Serif

Requirements
Must have
• Clean, professional look and feel, menu-driven navigation (tabular or similar). Please see the project brief for RGB codes for our firm color palette.
Nice to have
• Please refer to sample of paper reports for overall look and feel. Not necessary to replicate exactly, but web portal should coexist with our paper reports and firm website.
Should not have
• No whimsy animated gifs, trendy over the top graphics. Must be conservatively clean and not gimmicky.

```html
<!DOCTYPE html>
<html lang="en">
<head>
<meta charset="utf-8">
<title>Brenwick Capital Advisors – Asset Allocation History</title>
<link rel="stylesheet" href="https://fonts.googleapis.com/css2?family=Open+Sans:wght@400;600;700&display=swap">
<style>
  :root {
    --brand-blue: #33a6d7;
    --brand-grey: #aaaaaa;
    --brand-dark: #5c5c5c;
    --ink: #000000;
    --page-bg: #f1f1f1;
    --panel: #ffffff;
    --rule: #e3e3e3;
    --text-soft: #777777;
    --nav-text: #999999;
    --cash: #b0e04a;
    --fixed: #69d42c;
    --equity: #d00000;
    --alts: #b293f5;
  }
  * { box-sizing: border-box; margin: 0; padding: 0; }
  html, body { width: 1200px; height: 899px; overflow: hidden; }
  body {
    background: var(--page-bg);
    font-family: "Open Sans", Arial, sans-serif;
    position: relative;
  }
  .portal {
    position: absolute; left: 99px; top: 0; width: 1002px; height: 840px;
    background: var(--panel);
    box-shadow: 0 0 4px rgba(0,0,0,.12);
  }
  .site-header {
    position: absolute; left: 0; top: 0; width: 100%; height: 142px;
    border-bottom: 1px solid var(--rule);
  }
  .brand {
    position: absolute; left: 36px; top: 52px;
    color: var(--brand-blue); font-weight: 600; font-size: 19px; letter-spacing: 3px;
    display: flex; align-items: center; gap: 10px;
  }
  .brand-mark { width: 14px; height: 14px; background: var(--brand-blue); }
  .main-nav {
    position: absolute; right: 41px; top: 37px;
    display: flex; gap: 33px; list-style: none;
    font-size: 13px; color: var(--nav-text);
  }
  .page-title {
    position: absolute; right: 42px; top: 84px;
    display: flex; align-items: center; gap: 14px;
    color: var(--brand-blue); font-size: 22px; font-weight: 700; letter-spacing: .3px;
  }
  .client-name { position: absolute; left: 36px; top: 172px; color: var(--brand-blue); font-size: 15.5px; font-weight: 600; }
  .account-no { position: absolute; left: 38px; top: 195px; color: var(--brand-dark); font-size: 13px; }
  .strategy, .allocation-heading {
    position: absolute; left: 35px; color: var(--brand-dark); font-size: 24px; font-weight: 700;
  }
  .strategy { top: 237px; }
  .allocation-heading { top: 272px; }
  .allocation-heading .as-of { color: var(--brand-blue); font-size: 15.5px; font-weight: 600; }
  .pie { position: absolute; left: 66px; top: 340px; }
  .allocation-table {
    position: absolute; left: 509px; top: 327px; width: 433px;
    border: 1px solid #d6d6d6; border-top: none;
    display: grid; grid-template-columns: 192px 129px 112px;
    font-size: 13px; color: var(--text-soft);
  }
  .th {
    background: var(--brand-blue); color: #fff; height: 54px;
    display: flex; align-items: center; padding-left: 13px; line-height: 17px;
  }
  .th + .th { border-left: 1px solid rgba(255,255,255,.35); padding-left: 16px; }
  .td { height: 60px; display: flex; align-items: center; }
  .td.first-row { margin-top: 0; }
  .td.class { padding-left: 13px; gap: 10px; }
  .td.num { justify-content: flex-end; border-left: 1px solid var(--rule); }
  .td.mv { padding-right: 40px; }
  .td.pct { padding-right: 37px; }
  .pad-top { height: 10px; }
  .pad-top.ruled { border-left: 1px solid var(--rule); }
  .pad-bottom { height: 14px; }
  .pad-bottom.ruled { border-left: 1px solid var(--rule); }
  .swatch { width: 27px; height: 27px; flex: none; }
  .totals { grid-column: 1 / -1; border-top: 1px solid var(--rule); height: 70px; position: relative; }
  .totals span { position: absolute; }
  .label-total { left: 14px; top: 13px; color: var(--ink); font-weight: 600; }
  .label-other { left: 12px; top: 38px; }
  .value-total { right: 151px; top: 13px; color: var(--brand-blue); font-weight: 600; }
  .pct-total { right: 37px; top: 13px; color: var(--ink); font-weight: 600; }
  .total-assets { grid-column: 1 / -1; border-top: 1px solid var(--rule); height: 42px; padding: 11px 0 0 14px; color: var(--brand-blue); font-weight: 600; }
  .site-footer {
    position: absolute; left: 0; top: 783px; width: 100%; height: 57px;
    background: var(--brand-dark); color: #fff; font-size: 13px;
    display: flex; align-items: center; justify-content: center;
  }
</style>
</head>
<body>
<div class="portal">
  <header class="site-header">
    <div class="brand"><span class="brand-mark"></span>BRENWICK CAPITAL ADVISORS</div>
    <ul class="main-nav">
      <li>Home</li><li>Investment approach</li><li>Our Team</li>
      <li>Market Intelligence</li><li>In The Media</li><li>Contact us</li>
    </ul>
    <h1 class="page-title">
      <svg width="30" height="30" viewBox="0 0 30 30" aria-hidden="true">
        <circle cx="15" cy="15" r="15" fill="var(--brand-blue)"/>
        <path d="M12 9.5 L19 15 L12 20.5 Z" fill="#fff"/>
      </svg>
      ASSET ALLOCATION HISTORY
    </h1>
  </header>

  <p class="client-name">Daniel Harwood</p>
  <p class="account-no">Account number: 123456789</p>
  <h2 class="strategy">Investment Strategy: Growth and Income</h2>
  <h2 class="allocation-heading">Asset Allocation <span class="as-of">(as of March 31, 2015)</span></h2>

  <svg class="pie" width="400" height="410" viewBox="-200 -190 400 410" role="img" aria-label="Asset allocation pie chart">
    <defs>
      <radialGradient id="floorShadow">
        <stop offset="0" stop-color="#000" stop-opacity=".3"/>
        <stop offset="1" stop-color="#000" stop-opacity="0"/>
      </radialGradient>
    </defs>
    <ellipse cx="5" cy="185" rx="195" ry="27" fill="url(#floorShadow)"/>
    <g stroke="#fff" stroke-width="3" stroke-linejoin="round">
      <path d="M0,0 L32.1,-157.8 A161,161 0 1 1 -160.7,10.1 Z" fill="var(--fixed)"/>
      <path transform="translate(0.8,-8)" d="M0,0 L0,-161 A161,161 0 0 1 32.1,-157.8 Z" fill="var(--cash)"/>
      <path transform="translate(-9.8,1.7)" d="M0,0 L-160.7,10.1 A161,161 0 0 1 -147.3,-65 Z" fill="var(--equity)"/>
      <path transform="translate(-5.5,-8.4)" d="M0,0 L-147.3,-65 A161,161 0 0 1 0,-161 Z" fill="var(--alts)"/>
    </g>
  </svg>

  <div class="allocation-table" role="table">
    <div class="th">Asset Class</div>
    <div class="th">Market Value ($)</div>
    <div class="th">Percentage<br>Allocation (%)</div>

    <div class="pad-top"></div><div class="pad-top ruled"></div><div class="pad-top ruled"></div>

    <div class="td class"><span class="swatch" style="background:var(--cash)"></span>Cash and Equivalents</div>
    <div class="td num mv">13,129</div><div class="td num pct">3.2</div>

    <div class="td class"><span class="swatch" style="background:var(--fixed)"></span>Fixed Income</div>
    <div class="td num mv">289,687</div><div class="td num pct">70.8</div>

    <div class="td class"><span class="swatch" style="background:var(--equity)"></span>Equity</div>
    <div class="td num mv">30,930</div><div class="td num pct">7.6</div>

    <div class="td class"><span class="swatch" style="background:var(--alts)"></span>Alternatives</div>
    <div class="td num mv">75,220</div><div class="td num pct">18.4</div>

    <div class="pad-bottom"></div><div class="pad-bottom ruled"></div><div class="pad-bottom ruled"></div>

    <div class="totals">
      <span class="label-total">Total</span>
      <span class="label-other">Other Assets</span>
      <span class="value-total">408,966</span>
      <span class="pct-total">100.0</span>
    </div>
    <div class="total-assets">Total Assets</div>
  </div>

  <footer class="site-footer">
    Brenwick Capital Advisors&nbsp;|&nbsp;48 Alder Wharf&nbsp;|&nbsp;Boston MA 02110&nbsp;|&nbsp;617-555-0142&nbsp;|&nbsp;brenwickcapitaladvisors.example
  </footer>
</div>
</body>
</html>
```